Quillaro Business Cards

Will need a front and back design for a business card for Quillaro.
Can accept the final product as an illustrator file.
www.quillaro.com is the company website.

Target Market(s)

he target market are Chief Technology Officers and people in the tech field.

Industry/Entity Type

Business

Requirements
Must have
• - The business card must have on one of the sides
name
title
company
phone
email
website
The other side may be of some design, derivation of logo and or colors

```html
<!DOCTYPE html>
<html lang="en">
<head>
<meta charset="utf-8">
<title>Quillaro Business Card</title>
<link href="https://fonts.googleapis.com/css2?family=Montserrat:wght@700&family=Mulish:wght@300;400;800&display=swap" rel="stylesheet">
<style>
  :root {
    --navy: #0b1657;
    --ink-navy: #0c1a5a;
    --contact-blue: #1f4e9c;
    --title-blue: #2a56a0;
    --paper: #ffffff;
    --soft-grey: #efefef;
  }
  * { margin: 0; padding: 0; box-sizing: border-box; }
  html, body { width: 1200px; height: 726px; overflow: hidden; background: var(--paper); }
  .card {
    position: relative;
    width: 1200px;
    height: 726px;
    overflow: hidden;
    background: var(--paper);
    font-family: "Mulish", sans-serif;
  }
  .backdrop { position: absolute; inset: 0; }
  .brand-band {
    position: absolute;
    left: 0; top: 0;
    width: 203px; height: 726px;
    background: var(--navy);
  }
  .vertical {
    position: absolute;
    writing-mode: vertical-rl;
    transform: rotate(180deg);
    white-space: nowrap;
  }
  .brand-name {
    left: 50px; top: 236px; height: 440px;
    font-family: "Montserrat", sans-serif;
    font-weight: 700;
    font-size: 64px;
    line-height: 68px;
    letter-spacing: 0.04em;
    text-transform: uppercase;
    color: var(--paper);
  }
  .brand-tagline {
    left: 124px; top: 236px; height: 432px;
    font-family: "Montserrat", sans-serif;
    font-weight: 700;
    font-size: 18px;
    line-height: 24px;
    letter-spacing: 0.2em;
    text-transform: uppercase;
    color: var(--paper);
  }
  .person {
    left: 918px; top: 100px; height: 396px;
  }
  .person-name {
    font-weight: 800;
    font-size: 54px;
    line-height: 56px;
    color: var(--ink-navy);
  }
  .person-title {
    font-weight: 300;
    font-size: 26px;
    line-height: 30px;
    color: var(--title-blue);
  }
  .contact {
    left: 1046px; top: 30px; height: 466px;
    font-weight: 300;
    font-size: 27px;
    line-height: 31px;
    color: var(--contact-blue);
  }
  .contact-line { display: flex; }
  .contact-label { flex: 0 0 84px; }
</style>
</head>
<body>
  <div class="card">
    <svg class="backdrop" width="1200" height="726" viewBox="0 0 1200 726" role="img" aria-label="Large faint grey emblem artwork behind the contact details">
      <circle cx="760" cy="440" r="420" fill="var(--soft-grey)"/>
    </svg>

    <div class="brand-band"></div>
    <div class="vertical brand-name">Quillaro</div>
    <div class="vertical brand-tagline">Guarding Every Endpoint</div>

    <div class="vertical person">
      <div class="person-name">Daniel Marsh</div>
      <div class="person-title">Director</div>
    </div>

    <div class="vertical contact">
      <div class="contact-line"><span class="contact-label">Ph:</span><span>(555) 014-2738</span></div>
      <div class="contact-line"><span class="contact-label">E-mail:</span><span>d.marsh@quillaro.com</span></div>
      <div class="contact-line"><span class="contact-label">Web:</span><span>www.quillaro.com</span></div>
    </div>
  </div>
</body>
</html>
```